Torvale Wound Care Business card design

We need a business card designed around our logo which was provided. The logo of preference is the colored. Also the colors and fonts were provided.

Target Market(s)

Our Referral partners are home health agencies.

Industry/Entity Type

Healthcare

Contact Information for Business Card

Name , Phone #, Email , Title

Requirements
Nice to have
• Creativity
Should not have
• basic

```html
<!DOCTYPE html>
<html lang="en">
<head>
<meta charset="utf-8">
<title>Torvale Wound Care – Business Card</title>
<link href="https://fonts.googleapis.com/css2?family=Poppins:wght@400;500;600&display=swap" rel="stylesheet">
<style>
  :root {
    --stage: #0d77a6;
    --navy: #2c4898;
    --ink: #24408f;
    --sky: #1e9be6;
    --paper: #ffffff;
  }
  * { margin: 0; padding: 0; box-sizing: border-box; }
  html, body {
    width: 1200px; height: 900px; overflow: hidden;
    background: var(--stage);
    font-family: "Poppins", sans-serif;
  }
  .stage {
    width: 1200px; height: 900px;
    display: flex; flex-direction: column;
    align-items: center; justify-content: center; gap: 40px;
  }
  .card {
    position: relative;
    width: 700px; height: 400px;
    overflow: hidden;
    box-shadow: 0 12px 30px rgba(0, 0, 0, 0.25);
  }
  .card--front {
    background: var(--navy);
    display: flex; align-items: center; justify-content: center;
  }
  .brand { display: flex; align-items: center; gap: 14px; }
  .brand__mark { width: 34px; height: 34px; background: var(--sky); }
  .brand__name { font-weight: 500; color: var(--paper); font-size: 40px; letter-spacing: 0.5px; }

  .card--back { background: var(--paper); }
  .card--back .brand { position: absolute; top: 40px; right: 50px; gap: 10px; }
  .card--back .brand__mark { width: 22px; height: 22px; }
  .card--back .brand__name { color: var(--ink); font-size: 22px; }

  .rule { position: absolute; left: 0; width: 100%; }
  .rule--upper { top: 128px; height: 2px; background: var(--ink); }
  .rule--accent { top: 124px; left: 440px; width: 260px; height: 7px; background: var(--sky); }
  .rule--lower { top: 262px; height: 3px; background: var(--ink); }

  .person { position: absolute; left: 70px; top: 168px; }
  .person__name { color: var(--ink); font-size: 32px; font-weight: 400; line-height: 1.1; }
  .person__title {
    color: var(--sky); font-size: 13px; font-weight: 500;
    letter-spacing: 0.5px; text-transform: uppercase; text-align: right;
  }

  .contacts { position: absolute; left: 70px; top: 290px; list-style: none; }
  .contacts__item {
    display: flex; align-items: center; gap: 16px;
    color: var(--ink); font-size: 24px; margin-bottom: 14px;
  }
  .contacts__icon { width: 34px; height: 34px; flex: none; }
</style>
</head>
<body>
<main class="stage">
  <section class="card card--front" aria-label="Card front">
    <div class="brand">
      <span class="brand__mark"></span>
      <span class="brand__name">Torvale Wound Care</span>
    </div>
  </section>

  <section class="card card--back" aria-label="Card back">
    <div class="brand">
      <span class="brand__mark"></span>
      <span class="brand__name">Torvale Wound Care</span>
    </div>

    <div class="rule rule--upper"></div>
    <div class="rule rule--accent"></div>

    <div class="person">
      <p class="person__name">Name : Dr. Halvorsen</p>
      <p class="person__title">General Surgeon</p>
    </div>

    <div class="rule rule--lower"></div>

    <ul class="contacts">
      <li class="contacts__item">
        <svg class="contacts__icon" viewBox="0 0 34 34" aria-hidden="true">
          <circle cx="17" cy="17" r="17" fill="#1e9be6"/>
          <path d="M12 9c1 0 2 2.5 2.4 3.6.3.8-1.3 1.8-1.1 2.4.8 2 2.5 3.8 4.6 4.7.6.2 1.6-1.4 2.4-1.1 1.1.4 3.6 1.4 3.6 2.4 0 1.4-1.7 3-3.4 3C14.5 24 10 19.5 10 12.5 10 10.8 10.6 9 12 9z" fill="#fff"/>
        </svg>
        <span>362-555-0147</span>
      </li>
      <li class="contacts__item">
        <svg class="contacts__icon" viewBox="0 0 34 34" aria-hidden="true">
          <circle cx="17" cy="17" r="17" fill="#1e9be6"/>
          <rect x="9" y="11" width="16" height="12" rx="1.5" fill="none" stroke="#fff" stroke-width="1.8"/>
          <path d="M9.5 12l7.5 6 7.5-6" fill="none" stroke="#fff" stroke-width="1.8"/>
        </svg>
        <span>halvorsen@torvale.io</span>
      </li>
    </ul>
  </section>
</main>
</body>
</html>
```